Brent Sowle Director / Photographer Branding

I need note pads, envelops, business cards and letter head for my company. I'm a fashion and advertising director / photographer. I'm having trouble deciding how to include both Director & Photographer in my title or if it is even necessary. Maybe just my name is enough. I'm open for even using my initials if it works with the design and overall pieces. Please view my website to see what I have at this moment and what work I do. www.brentsowle.example
Updates

Project Deadline Extended
Reason: Hello Everyone! I'm extending the deadline since I have been traveling on a job out of country and I wanted to have more time to look through all the designs and give enough time for everyone to provide changes with designs and updates. I will be more available to communicate online now that I'm back in the office! Thank you! Brent Sowle

Target Market(s)

Fashion magazines, clothing lines and beauty cosmetic brands.

Industry/Entity Type

Fashion Photography

Font styles to use
Sans Serif

Colors
acd036
acd35d
cbcbcb
f5f5f5

Requirements
Must have
• My name.. Brent Sowle, my website: brentsowle.example my phone number, 555-284-6031
• I don't need my address on these. I also live by the philosophy that less is more and keeping things simple ads strength to a design. I also don't want to stop people from taking chances and experimenting with an idea that might take me down different road with my branding.
Nice to have
• Bold designs and clean lines. I'm open to ideas that I could adopt but I lean towards a more minimalistic look in general.
Should not have
• Not have cheesy graphics or pictures. No images of cameras, film or anything that looks like it is a camera or aperture, lens etc... ;)

```html
<!DOCTYPE html>
<html lang="en">
<head>
<meta charset="utf-8">
<title>Brent Sowle Letterhead</title>
<link rel="stylesheet" href="https://fonts.googleapis.com/css2?family=Exo+2:wght@300;400&family=Arimo:wght@400&display=swap">
<style>
  :root {
    --green: #acd036;
    --green-soft: #acd35d;
    --green-deep: #8db42f;
    --grey: #cbcbcb;
    --grey-light: #f5f5f5;
    --grey-dark: #6a6a6e;
    --ink: #1e1e1e;
    --paper: #ffffff;
    --backdrop: #e9eae6;
  }
  * { margin: 0; padding: 0; box-sizing: border-box; }
  html, body { width: 1094px; height: 1200px; overflow: hidden; }
  body { background: var(--backdrop); position: relative; }

  .letterhead {
    position: absolute; left: 140px; top: 25px;
    width: 813px; height: 1150px;
    background: var(--paper); overflow: hidden;
    box-shadow: 0 6px 24px rgba(0,0,0,.12);
  }
  .letterhead__arc { position: absolute; left: 0; top: 0; }

  .header-rule { position: absolute; top: 60px; height: 8px; }
  .header-rule--grey { left: 0; width: 125px; background: linear-gradient(#9a9a9e, var(--grey-dark)); }
  .header-rule--green { left: 276px; right: 0; background: var(--green); }

  .masthead { position: absolute; left: 132px; top: 47px; white-space: nowrap; }
  .masthead__name {
    font-family: "Exo 2", sans-serif; font-weight: 400;
    font-size: 16px; letter-spacing: 2px; color: var(--green); line-height: 1;
  }
  .masthead__title {
    font-family: "Arimo", sans-serif; font-size: 10.5px; color: #a9a9a9;
    margin-top: 3px; margin-left: 3px;
  }

  .name-column {
    position: absolute; left: 36px; top: 62px; width: 60px;
    display: flex; flex-direction: column; align-items: center;
    font-family: "Exo 2", sans-serif; font-weight: 300;
    font-size: 48px; line-height: 96px; color: var(--green);
  }

  .letter-body {
    position: absolute; left: 147px; top: 200px; width: 606px;
    font-family: "Arimo", sans-serif; font-size: 14px; line-height: 24px;
    color: var(--ink); letter-spacing: -0.45px;
  }
  .letter-body p + p { margin-top: 24px; }
  .letter-body p.spaced { margin-top: 48px; }

  .contact-band {
    position: absolute; left: 0; bottom: 0; width: 420px; height: 96px;
    border-top-right-radius: 40px;
    background: linear-gradient(var(--green-soft) 0%, var(--green) 35%, var(--green-deep) 100%);
    padding: 21px 0 0 48px;
    font-family: "Arimo", sans-serif; font-size: 15px; color: #fff; line-height: 26px;
    white-space: nowrap;
  }
  .contact-band__row { display: flex; align-items: center; }
  .contact-item { display: inline-flex; align-items: center; margin-right: 10px; }
  .contact-item svg { margin-right: 8px; flex: none; }
  .social-square { width: 11px; height: 11px; border: 1.6px solid #fff; margin-right: 8px; }
</style>
</head>
<body>
  <main class="letterhead">
    <svg class="letterhead__arc" width="813" height="1150" aria-hidden="true">
      <defs>
        <linearGradient id="arcShade" x1="0" y1="0" x2="1" y2="0">
          <stop offset="0" stop-color="#e4e4e6"/>
          <stop offset="1" stop-color="#f5f5f5"/>
        </linearGradient>
      </defs>
      <circle cx="-400" cy="470" r="680" fill="url(#arcShade)"/>
    </svg>

    <div class="header-rule header-rule--grey"></div>
    <div class="header-rule header-rule--green"></div>
    <header class="masthead">
      <div class="masthead__name">BRENT SOWLE</div>
      <div class="masthead__title">Director / Photographer</div>
    </header>

    <div class="name-column" aria-label="Brent Sowle">
      <span>B</span><span>R</span><span>E</span><span>N</span><span>T</span>
      <span>S</span><span>O</span><span>W</span><span>L</span><span>E</span>
    </div>

    <section class="letter-body">
      <p>Lorem Ipsum is simply dummy text of the printing and typesetting industry. Lorem Ipsum has been the industry’s standard dummy text ever since the 1500s, when an unknown printer took a galley of type and scrambled it to make a type specimen book. It has survived not only five centuries, but also the leap into electronic typesetting, remaining essentially unchanged. It was popularised in the 1960s with the release of Transfix sheets containing Lorem Ipsum passages, and more recently with desktop publishing software like Folio LayoutDesk including versions of Lorem Ipsum.</p>
      <p>It is a long established fact that a reader will be distracted by the readable content of a page when looking at its layout. The point of using Lorem Ipsum is that it has a more-or-less normal distribution of letters, as opposed to using ’Content here, content here’, making it look like readable English. Many desktop publishing packages and web page editors now use Lorem Ipsum as their default model text, and a search for ’lorem ipsum’ will uncover many web sites still in their infancy. Various versions have evolved over the years, sometimes by accident, sometimes on purpose (injected humour and the like).</p>
      <p class="spaced">Contrary to popular belief, Lorem Ipsum is not simply random text. It has roots in a piece of classical Latin literature from 45 BC, making it over 2000 years old. Henrik Vallmoor, a Latin professor at Ashford Vale College in Oregon, looked up one of the more obscure Latin words, consectetur, from a Lorem Ipsum passage, and going through the cites of the word in classical literature, discovered the undoubtable source. Lorem Ipsum comes from sections 1.10.32 and 1.10.33 of "de Finibus Bonorum et Malorum" structures, to generate Lorem Ipsum which looks reasonable. The generated Lorem Ipsum is therefore always free from repetition, injected humour, or non-characteristic words etc.</p>
    </section>

    <footer class="contact-band">
      <div class="contact-band__row">
        <span class="contact-item">
          <svg width="12" height="9" viewBox="0 0 12 9" aria-hidden="true"><rect width="12" height="9" rx="1" fill="#fff"/><path d="M0.5 1 L6 5 L11.5 1" stroke="#9cc232" stroke-width="1.2" fill="none"/></svg>
          brent@brentsowle.example
        </span>
        <span class="contact-item">
          <svg width="11" height="12" viewBox="0 0 24 24" aria-hidden="true"><path fill="#fff" d="M6.6 10.8a15.1 15.1 0 0 0 6.6 6.6l2.2-2.2c.3-.3.7-.4 1-.2 1.1.4 2.3.6 3.6.6.6 0 1 .4 1 1V20c0 .6-.4 1-1 1A17 17 0 0 1 3 4c0-.6.4-1 1-1h3.5c.6 0 1 .4 1 1 0 1.3.2 2.5.6 3.6.1.3 0 .7-.2 1z"/></svg>
          555-284-6031
        </span>
      </div>
      <div class="contact-band__row">
        <span class="contact-item">
          <svg width="12" height="12" viewBox="0 0 12 12" aria-hidden="true"><circle cx="6" cy="6" r="5.3" fill="none" stroke="#fff" stroke-width="1.3"/><path d="M0.8 6h10.4M6 0.8c-2.4 2.8-2.4 7.6 0 10.4M6 0.8c2.4 2.8 2.4 7.6 0 10.4" stroke="#fff" stroke-width="1" fill="none"/></svg>
          www.brentsowle.example
        </span>
        <span class="contact-item"><span class="social-square"></span>@brentsowle</span>
      </div>
    </footer>
  </main>
</body>
</html>
```